Pelican Litigation Funding Letterhead & Document Template

We need a letter head designed for our fund. Our fund works with law firms and investors across the globe. We need a a cover letter template as well as a document template for subsequent pages. Blue and white color scheme is preferred. This is our predecessor's website: https://www.pelicanvq.com/index.html. Please see our logo attached. The logo color code is #19478d. Font is Gotham-Medium.
Target Market(s)
Sophisticated investors and law firms
Font styles to use
Sans Serif
Colors
0255a3

```html
<!DOCTYPE html>
<html lang="en">
<head>
<meta charset="utf-8">
<title>Pelican Litigation Funding Letterhead</title>
<link rel="stylesheet" href="https://fonts.googleapis.com/css2?family=Open+Sans:wght@400;600&family=Arimo:wght@700&display=swap">
<style>
  :root {
    --brand-blue: #19478d;
    --footer-blue: #0b3f8c;
    --rule-grey: #a3a3a3;
    --text-grey: #4a4a4a;
    --heading-grey: #555555;
    --paper: #fafafa;
    --ink: #1c1c1c;
  }
  * { margin: 0; padding: 0; box-sizing: border-box; }
  html, body { width: 1059px; height: 1200px; overflow: hidden; background: var(--paper); }
  .letterhead {
    position: relative;
    width: 1059px;
    height: 1200px;
    background: var(--paper);
    font-family: "Open Sans", Arial, sans-serif;
    color: var(--text-grey);
  }
  .brand {
    position: absolute;
    left: 77px;
    top: 40px;
    width: 300px;
    height: 110px;
    display: flex;
    align-items: center;
    gap: 12px;
  }
  .brand-mark {
    width: 18px;
    height: 18px;
    background: var(--brand-blue);
    flex-shrink: 0;
  }
  .brand-name {
    font-weight: 600;
    font-size: 22px;
    line-height: 1.2;
    color: var(--brand-blue);
  }
  .contact {
    position: absolute;
    left: 727px;
    top: 42px;
    font-size: 16px;
    color: var(--ink);
  }
  .contact-phone {
    display: flex;
    align-items: center;
    gap: 10px;
    font-size: 14px;
    line-height: 21px;
  }
  .contact-phone svg { width: 12px; height: 12px; fill: var(--brand-blue); }
  .contact-address {
    margin-top: 4px;
    border-left: 2px solid var(--brand-blue);
    padding-left: 14px;
    margin-left: 4px;
    line-height: 25px;
  }
  .letter {
    position: absolute;
    left: 91px;
    top: 276px;
    width: 888px;
  }
  .salutation {
    font-family: "Arimo", Arial, sans-serif;
    font-weight: 700;
    font-size: 22px;
    color: var(--heading-grey);
    margin-bottom: 22px;
  }
  .letter p {
    font-size: 18.5px;
    line-height: 27.5px;
    text-align: justify;
    margin-bottom: 27px;
  }
  .signature {
    position: absolute;
    left: 91px;
    top: 1000px;
    width: 200px;
    height: 80px;
    background: linear-gradient(90deg, #e4e4e4, #d6d6d6);
  }
  .footer {
    position: absolute;
    left: 0;
    bottom: 0;
    width: 1059px;
    height: 40px;
  }
  .footer svg { display: block; }
  .footer-url {
    position: absolute;
    left: 783px;
    top: 9px;
    font-size: 16px;
    letter-spacing: 1.5px;
    color: #ffffff;
  }
</style>
</head>
<body>
<main class="letterhead">
  <header>
    <div class="brand">
      <span class="brand-mark"></span>
      <span class="brand-name">Pelican Litigation Funding</span>
    </div>
    <address class="contact" style="font-style:normal">
      <div class="contact-phone">
        <svg viewBox="0 0 12 12" aria-hidden="true"><path d="M2.4 0.5 L4.2 2.6 L3.2 4 C3.9 5.6 5.3 7.2 7.6 8.6 L8.9 7.6 L11.2 9.5 L9.6 11.5 C5 11 1 7 0.5 2.3 Z"/></svg>
        <span>(713) 555-0142</span>
      </div>
      <div class="contact-phone">
        <svg viewBox="0 0 12 12" aria-hidden="true"><path d="M3 0 H8 L9 1.5 V4 H3 Z M1 5 H11 V9.5 H1 Z M2.5 10 H9.5 V12 H2.5 Z"/></svg>
        <span>(713) 555-0143</span>
      </div>
      <div class="contact-address">
        Linden Court - Penthouse Floor<br>
        4810 Harlow Avenue, Suite 1200<br>
        Houston, Texas 77019
      </div>
    </address>
  </header>

  <section class="letter">
    <h1 class="salutation">Dear Mr. Carter,</h1>
    <p>Lorem Ipsum is simply dummy text of the printing and typesetting industry. Lorem Ipsum has been the industry's standard dummy text ever since the 1500s, when an unknown printer took a galley of type and scrambled it to make a type specimen book. It has survived not only five centuries, but also the leap into electronic typesetting, remaining essentially unchanged.</p>
    <p>The standard chunk of Lorem Ipsum used since the 1500s is reproduced below for those interested. Sections 1.10.32 and 1.10.33 from "de Finibus Bonorum et Malorum" by Tullius Verro are also reproduced in their exact original form, accompanied by English versions from the 1914 translation by H. Ashby</p>
    <p>Lorem Ipsum is simply dummy text of the printing and typesetting industry. Lorem Ipsum has been the industry's standard dummy text ever since the 1500s, when an unknown printer took a galley of type and scrambled it to make a type specimen book. It has survived not only five centuries, but also the leap into electronic typesetting, remaining essentially unchanged. It was popularised in the</p>
    <p>The standard chunk of Lorem Ipsum used since the 1500s is reproduced below for those interested. Sections 1.10.32 and 1.10.33 from "de Finibus Bonorum et Malorum" by Tullius Verro are also reproduced in their exact original form, accompanied by English versions from the 1914 translation by H. Ashby</p>
  </section>

  <div class="signature" role="img" aria-label="Handwritten signature of the sender"></div>

  <footer class="footer">
    <svg width="1059" height="40" viewBox="0 0 1059 40" aria-hidden="true">
      <path d="M0 4 H728 C712 13 700 16 676 16 H0 Z" fill="var(--rule-grey)"/>
      <rect x="0" y="28" width="760" height="12" fill="var(--footer-blue)"/>
      <path d="M694 40 C730 40 748 0 800 0 H1059 V40 Z" fill="var(--footer-blue)"/>
      <path d="M676 28 C712 28 726 6 760 6 L768 6 C738 6 724 28 694 28 Z" fill="var(--paper)" opacity="0"/>
    </svg>
    <span class="footer-url">www.pelicanvq.com</span>
  </footer>
</main>
</body>
</html>
```